Book cover design for the book titled "Quieter Under Lanterns."

create a book cover. The book title is, "Quieter Under Lanterns: A Ledger of Harbour Songs Across Mild Winters." The purpose of the book is to create awareness of how childhood trauma is impacting 7 out of 10 adults in the world today and that two-thirds of children will experience neglect and or abuse before their 18th birthday. One victim described that his mental and physical illness resulting from childhood trauma felt like he wa being pulled to the ground, that the force was "quieter under lanterns." The design should be clean and simple and communicate a crisis.

```html
<!DOCTYPE html>
<html lang="en">
<head>
<meta charset="UTF-8">
<title>Quieter Under Lanterns — Book Cover</title>
<link href="https://fonts.googleapis.com/css2?family=Cinzel:wght@500;600&family=Montserrat:wght@700&family=Mrs+Saint+Delafield&display=swap" rel="stylesheet">
<style>
  :root {
    --stage: #000000;
    --sky-top: #93d5e3;
    --sky-mid: #c4e8f0;
    --sky-low: #eef4fb;
    --title-blue: #0b4a93;
    --ink: #111111;
    --alarm-red: #c4161c;
    --wood-light: #e8cfa6;
    --wood-dark: #c9a677;
  }
  html, body {
    margin: 0;
    padding: 0;
    width: 1200px;
    height: 1200px;
    overflow: hidden;
    background: var(--stage);
  }
  .canvas {
    position: relative;
    width: 1200px;
    height: 1200px;
    background: var(--stage);
  }
  .book-cover {
    position: absolute;
    left: 360px;
    top: 240px;
    width: 480px;
    height: 720px;
    overflow: hidden;
    background: linear-gradient(180deg, var(--sky-top) 0%, var(--sky-mid) 38%, var(--sky-low) 62%, var(--sky-low) 100%);
  }
  .title {
    margin: 0;
    position: absolute;
    left: 0;
    top: 0;
    width: 100%;
    height: 400px;
    color: var(--title-blue);
    font-family: "Cinzel", "Trajan Pro", serif;
    font-weight: 600;
  }
  .title-word {
    position: absolute;
    left: 0;
    width: 100%;
    text-align: center;
    line-height: 1;
    letter-spacing: -1px;
  }
  .title-word--top { top: 70px; font-size: 88px; }
  .title-word--bottom { top: 289px; font-size: 76px; }
  .title-link {
    position: absolute;
    left: 0;
    top: 190px;
    width: 100%;
    text-align: center;
    color: var(--ink);
    font-family: "Mrs Saint Delafield", cursive;
    font-weight: 400;
    font-size: 112px;
    line-height: 1;
  }
  .figure-art {
    position: absolute;
    left: 46px;
    top: 443px;
    width: 76px;
    height: 139px;
    border-radius: 36px 36px 4px 4px;
    background: linear-gradient(135deg, var(--wood-light), var(--wood-dark));
  }
  .subtitle {
    position: absolute;
    left: 146px;
    top: 450px;
    margin: 0;
    font-family: "Montserrat", "Helvetica Neue", Arial, sans-serif;
    font-weight: 700;
    font-size: 30px;
    line-height: 42px;
    color: var(--ink);
    letter-spacing: -0.3px;
  }
  .subtitle .accent { color: var(--alarm-red); }
  .author {
    position: absolute;
    left: 0;
    top: 620px;
    width: 100%;
    margin: 0;
    text-align: center;
    font-family: "Cinzel", "Trajan Pro", serif;
    font-weight: 600;
    font-size: 50px;
    line-height: 1;
    color: var(--ink);
    letter-spacing: -0.5px;
  }
</style>
</head>
<body>
<main class="canvas">
  <section class="book-cover" aria-label="Book cover">
    <h1 class="title">
      <span class="title-word title-word--top">QUIETER</span>
      <span class="title-word title-word--bottom">LANTERNS</span>
    </h1>
    <div class="title-link" aria-hidden="true">Under</div>
    <div class="figure-art" role="img" aria-label="Small wooden figure of a person with a smaller figure cut out and fallen at its feet"></div>
    <p class="subtitle">
      A <span class="accent">Ledger</span> of<br>
      <span class="accent">Harbour</span> Songs<br>
      <span class="accent">Across Mild Winters</span>
    </p>
    <p class="author">AUTHOR NAME</p>
  </section>
</main>
</body>
</html>
```